Flyer-Design für Dekorations- und Farbkonzepte
hat alles bestens geklappt und tolles Design...kann Sie nur weiterempfehlen! PS. Lieben Dank für die Geduld! Beste Grüsse Rosalie Trachsler
Zielgruppe
Dekorationskonzepte, Farbkonzepte für Räume, Planung und Realisation Geschäfts - und Privatkunden, Zielgruppe Firmen, Seniorenheime , Privatkundschaft
Aufgabenstellung
Ich bin im Mai an einem Anlass in einem Seniorenheim und habe die Möglichkeit mich zu präsentieren , ich mache an diesem Anlass die Dekoration und möchte dabei Tag einen wertigen Flyer abgeben. An diesem Anlass sind auch der Gemeindepräsident und Angehörige der Bewohner etc . eingeladen. Der Flyer soll etwas gediegen daherkommen und über meine Arbeit informieren. Ich möchte vorallem Geschäftskunden ansprechen. Der Flyer sollte Emotionen wecken. Masse ca. A5 ..bin da sehr offen (nicht zu klein )

```html
<!DOCTYPE html>
<html lang="de">
<head>
<meta charset="utf-8">
<title>Stillraum – Kontakt</title>
<link rel="stylesheet" href="https://fonts.googleapis.com/css2?family=Fira+Sans+Extra+Condensed:wght@200;300&display=swap">
<style>
  :root {
    --paper: #ffffff;
    --panel: #7e8ea3;
    --ink: #ffffff;
  }
  html, body {
    margin: 0;
    padding: 0;
    width: 846px;
    height: 1200px;
    overflow: hidden;
    background: var(--paper);
  }
  .flyer-back {
    position: relative;
    width: 846px;
    height: 1200px;
    background: var(--paper);
    font-family: "Fira Sans Extra Condensed", "Arial Narrow", sans-serif;
    color: var(--ink);
  }
  .color-panel {
    position: absolute;
    left: 28px;
    top: 28px;
    width: 790px;
    height: 1157px;
    background: var(--panel);
  }
  .brand-name {
    position: absolute;
    left: 60px;
    top: 140px;
    margin: 0;
    font-weight: 200;
    font-size: 62px;
    line-height: 1;
    letter-spacing: 0.42em;
  }
  .contact {
    position: absolute;
    left: 62px;
    margin: 0;
    font-weight: 300;
    font-size: 32px;
    line-height: 39px;
    font-style: normal;
  }
  .contact-address { top: 280px; }
  .contact-phone { top: 435px; }
  .contact-online { top: 512px; line-height: 43px; }
  .contact a { color: inherit; text-decoration: none; }
</style>
</head>
<body>
  <div class="flyer-back">
    <div class="color-panel"></div>
    <h1 class="brand-name">STILLRAUM</h1>
    <address class="contact contact-address">
      Stillraum Rosalie Trachsler<br>
      Lindenweg 14<br>
      CH-3125 Talbach
    </address>
    <p class="contact contact-phone">Tel. 079 412 68 35</p>
    <p class="contact contact-online">
      <a href="mailto:welcome@stillraum.ch">welcome@stillraum.ch</a><br>
      <a href="https://www.stillraum.ch">www.stillraum.ch</a>
    </p>
  </div>
</body>
</html>
```